I need a label with logo to go on jars of honey.
Label size 70mm x 70mm
The front label should say :
The Tall Fern Honey Co. (logo)
Tarepo Honey
400g
The back label:
Would have nutritional information
And our address
You can see from the uploaded files the styles I prefer, I have uploaded a photo of the honey product too. The background of the logo doesn't have to be white. I would like to develop a color scheme that would look nice against the color of the honey.
Logo Text
The Tall Fern Honey Co. / The Tall Fern Honey Company

```html
<!DOCTYPE html>
<html lang="en">
<head>
<meta charset="utf-8">
<title>Tarepo Honey – Front Label</title>
<link href="https://fonts.googleapis.com/css2?family=Tinos&display=swap" rel="stylesheet">
<style>
  :root {
    --page-bg: #f7f7f7;
    --honey-orange: #f5860e;
    --honey-mid: #fbb46a;
    --honey-pale: #fde3c6;
    --label-white: #ffffff;
    --ink-brown: #8b5844;
    --label-shadow: rgba(0, 0, 0, 0.35);
  }
  html, body {
    margin: 0;
    padding: 0;
    width: 1200px;
    height: 1200px;
    overflow: hidden;
    background: var(--page-bg);
  }
  .canvas {
    position: relative;
    width: 1200px;
    height: 1200px;
    display: flex;
    align-items: center;
    justify-content: center;
  }
  .front-label {
    position: relative;
    width: 980px;
    height: 876px;
    background: linear-gradient(
      to bottom,
      var(--honey-orange) 0%,
      var(--honey-mid) 38%,
      var(--honey-pale) 62%,
      var(--label-white) 85%,
      var(--label-white) 100%
    );
    box-shadow: 14px 22px 30px var(--label-shadow);
    font-family: "Tinos", "Times New Roman", serif;
    color: var(--ink-brown);
  }
  .front-label > * {
    position: absolute;
    left: 50%;
    transform: translate(-50%, -50%);
    margin: 0;
    white-space: nowrap;
    text-align: center;
    font-weight: 400;
  }
  .brand-name {
    top: 222px;
    font-size: 58px;
    line-height: 1.2;
  }
  .product-name {
    top: 447px;
    font-size: 42px;
  }
  .net-weight {
    top: 803px;
    font-size: 31px;
  }
</style>
</head>
<body>
  <main class="canvas">
    <section class="front-label">
      <p class="brand-name">The Tall Fern<br>Honey Company</p>
      <h1 class="product-name">Tarepo Honey</h1>
      <p class="net-weight">400g</p>
    </section>
  </main>
</body>
</html>
```